Brightmoor Signal needs a Business Card

Designers!
More often than not, people want a cheap business card and often argue "I only want 100, not 500" - Years ago I worked in print and always wanted a client to ask for something that challenged me and would be great for my portfolio.

Years have past, and I dont have the time to do it myself so I'd love to see what everyone can offer.

Reason: Hey Guys, The designs are looking good but i've extended it a few more days as I wont be near a laptop and i'm trying to provide everyone feedback - Sorry!

Target Market(s)

Key decision makers, Potential Clients, Networking events and opportunities.

Industry/Entity Type

Business

Requirements
Must have
• Typography is very important. The type of paper is important.
The print, the shape. The creativity.
I'm very inspired by the below link
http://www.palevantro.com/blog/business-card-design/

Nice to have
• Stencelled cutouts. Embossing, nice typography.
I'd like the business card to be a conversation piece itself.

Attached is an image of business cards i've had in the past.
Additionally, some logos i've recently had designed by Quillmarsh.

```html
<!DOCTYPE html>
<html lang="en">
<head>
<meta charset="utf-8">
<title>Brightmoor Signal – Business Card</title>
<link href="https://fonts.googleapis.com/css2?family=Quicksand:wght@400;500;600&display=swap" rel="stylesheet">
<style>
  :root {
    --backdrop: #1f5a7e;
    --card: #171d2c;
    --ink-light: #ffffff;
    --ink-muted: #b9bec8;
    --accent: #8ee41f;
    --rule: #6b7180;
    --icon-tile: #0f131d;
  }
  html, body {
    margin: 0;
    padding: 0;
    width: 1200px;
    height: 900px;
    overflow: hidden;
    background: var(--backdrop);
    font-family: "Quicksand", sans-serif;
  }
  .card {
    position: absolute;
    left: 100px;
    top: 160px;
    width: 1000px;
    height: 580px;
    background: var(--card);
    border-radius: 4px;
    box-shadow: 0 10px 30px rgba(0, 0, 0, 0.35);
  }
  .brand {
    position: absolute;
    left: 0;
    right: 0;
    top: 170px;
    display: flex;
    flex-direction: column;
    align-items: center;
  }
  .brand-name {
    display: flex;
    align-items: center;
    gap: 22px;
  }
  .brand-mark {
    width: 26px;
    height: 26px;
    background: var(--accent);
  }
  .brand-title {
    margin: 0;
    color: var(--ink-light);
    font-weight: 500;
    font-size: 54px;
    letter-spacing: 2px;
    text-transform: uppercase;
    line-height: 1;
  }
  .brand-url {
    margin-top: 18px;
    padding-top: 12px;
    border-top: 1px solid var(--rule);
    color: var(--ink-muted);
    font-weight: 400;
    font-size: 22px;
    letter-spacing: 9px;
  }
  .contacts {
    position: absolute;
    left: 60px;
    right: 60px;
    bottom: 60px;
    display: flex;
    justify-content: space-between;
    align-items: center;
    list-style: none;
    margin: 0;
    padding: 0;
  }
  .contact {
    display: flex;
    align-items: center;
    gap: 18px;
    color: var(--accent);
    font-weight: 500;
    font-size: 24px;
    letter-spacing: 0.5px;
  }
  .contact-icon {
    width: 34px;
    height: 34px;
    flex: none;
  }
  .contact-tile {
    width: 34px;
    height: 34px;
    background: var(--icon-tile);
    display: flex;
    align-items: center;
    justify-content: center;
  }
  .contact-tile span {
    width: 14px;
    height: 14px;
    background: var(--accent);
  }
</style>
</head>
<body>
  <section class="card" aria-label="Brightmoor Signal business card">
    <div class="brand">
      <div class="brand-name">
        <span class="brand-mark" aria-hidden="true"></span>
        <h1 class="brand-title">Brightmoor Signal</h1>
      </div>
      <div class="brand-url">brightmoorsignal.com.au</div>
    </div>

    <ul class="contacts">
      <li class="contact">
        <svg class="contact-icon" viewBox="0 0 34 34" aria-hidden="true">
          <circle cx="17" cy="17" r="16" fill="var(--accent)"/>
          <g fill="none" stroke="var(--card)" stroke-width="1.6">
            <circle cx="17" cy="17" r="9"/>
            <ellipse cx="17" cy="17" rx="4" ry="9"/>
            <line x1="8" y1="17" x2="26" y2="17"/>
            <line x1="10" y1="12" x2="24" y2="12"/>
            <line x1="10" y1="22" x2="24" y2="22"/>
          </g>
        </svg>
        <span>brightmoorsignal.au</span>
      </li>
      <li class="contact">
        <span class="contact-tile" aria-hidden="true"><span></span></span>
        <span>@Mara_id</span>
      </li>
      <li class="contact">
        <span class="contact-tile" aria-hidden="true"><span></span></span>
        <span>Mara/social</span>
      </li>
    </ul>
  </section>
</body>
</html>
```